Varolta Business Card

I am looking for a business card design for a start-up company called Varolta Group. This is a management consultancy focused on sales, marketing, sales management, product management and AGILE software development. Our primary customers are $1M to $50M in revenue.

Varolta is the Italian word for "slope."

The path from $0 to $50M has many different growth stages associated with it. Each one having a significant slope to the next plateau. Our expertise helps our customers ascend each of those slopes. We bring experience, successful track-records in growing companies, best practices and a dive-in and roll-up your sleeves mentality. We are not sitting at base camp shouting instructions, we are right there with you, on the climb.

Industry/Entity Type

Business

```html
<!DOCTYPE html>
<html lang="en">
<head>
<meta charset="utf-8">
<title>Varolta Business Card</title>
<link href="https://fonts.googleapis.com/css2?family=Arimo:wght@400;700&display=swap" rel="stylesheet">
<style>
  :root {
    --backdrop: #e9eaea;
    --card: #f7f7f5;
    --ink: #56636c;
    --divider: #8a949a;
    --band-blue: #1a6fae;
    --band-green: #4c7d2a;
    --mark-blue: #1d6fae;
  }
  * { box-sizing: border-box; margin: 0; padding: 0; }
  html, body { width: 1200px; height: 1000px; overflow: hidden; }
  body {
    background: var(--backdrop);
    font-family: "Arimo", Arial, sans-serif;
    color: var(--ink);
    position: relative;
  }
  .card {
    position: absolute;
    left: 250px;
    width: 700px;
    height: 400px;
    background: var(--card);
    box-shadow: 0 2px 8px rgba(0,0,0,0.12);
    overflow: hidden;
  }
  .card--front { top: 70px; }
  .card--back { top: 530px; }

  .brand {
    display: flex;
    align-items: center;
    gap: 18px;
  }
  .brand-dot {
    width: 54px; height: 54px;
    border-radius: 50%;
    background: var(--mark-blue);
    flex: none;
  }
  .brand-name {
    font-weight: 400;
    color: var(--ink);
    letter-spacing: -1px;
    line-height: 1;
  }
  .card--front .brand {
    position: absolute;
    left: 50%; top: 50%;
    transform: translate(-50%, -50%);
  }
  .card--front .brand-name { font-size: 64px; }

  .card--back .brand {
    position: absolute;
    left: 60px; top: 60px;
    flex-direction: column;
    align-items: center;
    gap: 14px;
  }
  .card--back .brand-dot { width: 90px; height: 90px; }
  .card--back .brand-name { font-size: 60px; }

  .divider {
    position: absolute;
    left: 330px; top: 80px;
    width: 1px; height: 170px;
    background: var(--divider);
  }

  .contact {
    position: absolute;
    right: 40px; top: 74px;
    text-align: right;
  }
  .contact-name { font-size: 30px; font-weight: 700; line-height: 1.05; }
  .contact-role { font-size: 19px; letter-spacing: 1px; margin-bottom: 12px; }
  .contact-list { list-style: none; }
  .contact-list li {
    font-size: 19px;
    line-height: 30px;
    display: flex;
    justify-content: flex-end;
    align-items: center;
    gap: 12px;
  }
  .contact-list svg { width: 16px; height: 16px; flex: none; }

  .footer-band {
    position: absolute;
    left: 0; bottom: 0;
    width: 700px; height: 80px;
    background: linear-gradient(180deg, var(--band-blue) 0%, var(--band-green) 100%);
  }
</style>
</head>
<body>

  <section class="card card--front" aria-label="Card front">
    <div class="brand">
      <span class="brand-dot"></span>
      <span class="brand-name">Varolta</span>
    </div>
  </section>

  <section class="card card--back" aria-label="Card back">
    <div class="brand">
      <span class="brand-dot"></span>
      <span class="brand-name">Varolta</span>
    </div>

    <div class="divider"></div>

    <div class="contact">
      <p class="contact-name">Your Name</p>
      <p class="contact-role">POSITION</p>
      <ul class="contact-list">
        <li>000 000 000
          <svg viewBox="0 0 16 16" aria-label="phone"><path d="M4 1 L6 4 L5 6 Q6 9 10 11 L12 10 L15 12 L13 15 Q6 14 2 6 Q1 3 4 1 Z" fill="none" stroke="currentColor" stroke-width="1.3"/></svg>
        </li>
        <li>000 000 000
          <svg viewBox="0 0 16 16" aria-label="mobile"><rect x="4" y="1" width="8" height="14" rx="1" fill="none" stroke="currentColor" stroke-width="1.3"/><line x1="7" y1="12.5" x2="9" y2="12.5" stroke="currentColor" stroke-width="1.3"/></svg>
        </li>
        <li>000@000000
          <svg viewBox="0 0 16 16" aria-label="email"><rect x="1" y="3" width="14" height="10" fill="none" stroke="currentColor" stroke-width="1.3"/><path d="M1 3 L8 9 L15 3" fill="none" stroke="currentColor" stroke-width="1.3"/></svg>
        </li>
        <li>www.00000000000
          <svg viewBox="0 0 16 16" aria-label="website"><path d="M3 1 L13 9 L8.5 9.5 L11 14.5 L9 15.3 L6.7 10.5 L3 13.5 Z" fill="none" stroke="currentColor" stroke-width="1.2"/></svg>
        </li>
      </ul>
    </div>

    <div class="footer-band" role="img" aria-label="Decorative blue and green slope band along the card foot"></div>
  </section>

</body>
</html>
```